Brochure Design for Marketing Firm in Melbourne

We are a boutique growth marketing firm based in Melbourne, Australia called Brindle Harbor Partners. We are a team of marketing and branding specialists who invest in marketing for businesses who exhibit strong growth potential and work collaboratively to achieve this.

Our business has a number of capabilities which we call the "Product Tool Suite". We utilise these product tools to grow our client's businesses through customer acquisition, sales, media investment etc. We require a designer to develop 13 brochures in line with the Brindle Harbor Partners Branding and colour palette.

The tools are listed below:
1. Brand Archetype Tool
2. Brand Audit Tool
3. Business Canvas
4. Call Centre Performance Tool
5. Communication Messaging Tool
6. Growth Audit Tool
7. Loyalty Program
8. Media Leverage Program
9. Product Optimisation Tool
10. Referral Tool
11. Sales Coaching/Training Tool
12. Segmentation Tool
13. Social Media Process

In order to select a designer, we invite designers to produce a mock up of one Tool in a brochure layout. Once we have chosen the winning design we will contract the designer to produce the remaining 12 brochures using that design.

Ideally we would like to each brochure to be 2 pages (back and front) but we understand that some tools may require 3 or 4 pages.

Please refer to the files that we have uploaded containing
- our logo
- copy (text)
- a PDF of our own attempt (please refer to this for design inspiration, they are photoshop compatible)
- Accompanying visuals (graphs, photos logos etc.)

The final design should communicate financial growth and our corporate identity. The style should have a professional and modern feel that is clean and crisp.

Target Market(s)

Our clients include businesses with a proven track record looking for further marketing investment to grow their business

Industry/Entity Type

Investment

Requirements
Must have
• The designs must feature:

- The Brindle Harbor Partners logo
- The Brindle Harbor Lantern
- Content (this is text combined with graphs and flowcharts which we have provided)

Please refer to the pdf uploaded to see the suggested design approach.

```html
<!DOCTYPE html>
<html lang="en">
<head>
<meta charset="utf-8">
<title>Brand Archetype Tool – Brindle Harbor Partners</title>
<link rel="stylesheet" href="https://fonts.googleapis.com/css2?family=Bebas+Neue&family=Arimo:wght@400;700&family=Open+Sans:wght@400;700&display=swap">
<style>
  :root {
    --slate: #2e3e4b;
    --paper: #e4e5e7;
    --ink: #262626;
    --sky: #5aa9c9;
    --white: #ffffff;
    --muted: #3c4b57;
    --brand-blue: #5b9fc4;
  }
  * { margin: 0; padding: 0; box-sizing: border-box; }
  html, body { width: 1200px; height: 850px; overflow: hidden; background: var(--white); }
  .spread { position: relative; width: 1200px; height: 850px; }
  .page { position: absolute; top: 17px; width: 576px; height: 813px; overflow: hidden; background: var(--paper); }
  .page--front { left: 19px; }
  .page--back { left: 605px; }

  /* Front page */
  .cover-panel { position: absolute; left: 0; top: 0; width: 287px; height: 627px; background: var(--slate); }
  .cover-title {
    position: absolute; left: 37px; top: 330px;
    transform-origin: 0 0; transform: rotate(-90deg);
    font-family: "Bebas Neue", "Oswald", sans-serif;
    font-size: 88px; line-height: 70px; color: var(--white);
    white-space: nowrap; letter-spacing: 1px;
  }
  .cover-emblem { position: absolute; left: 0; top: 400px; width: 175px; height: 295px; }
  .cover-band { position: absolute; left: 0; top: 627px; width: 100%; height: 186px; background: var(--ink); }
  .cover-photo { position: absolute; left: 287px; top: 627px; width: 289px; height: 186px; }
  .wordmark {
    font-family: "Arimo", Arial, sans-serif; font-weight: 700;
    color: var(--slate); display: flex; align-items: center; gap: 8px; white-space: nowrap;
  }
  .wordmark__dot { width: 12px; height: 12px; background: var(--brand-blue); }
  .cover-logo { position: absolute; left: 325px; top: 558px; font-size: 19px; }

  /* Back page */
  .info-block { position: absolute; font-family: "Arimo", Arial, sans-serif; }
  .info-block h2 { font-size: 21.5px; line-height: 23px; font-weight: 700; margin-bottom: 4px; }
  .info-block p { font-size: 12px; line-height: 13.5px; }
  .info-block--intro { left: 319px; top: 86px; width: 235px; color: var(--slate); }
  .info-block--intro p { color: #1e1e1e; }
  .info-box { position: absolute; left: 288px; width: 289px; background: var(--sky); color: var(--white); padding: 18px 20px 0 32px; }
  .info-box--when { top: 240px; height: 167px; }
  .info-box--who { top: 462px; height: 165px; }
  .back-band { position: absolute; left: 0; top: 627px; width: 100%; height: 186px; background: var(--ink); }
  .back-logo { position: absolute; left: 33px; top: 28px; font-size: 23px; color: var(--brand-blue); }
  .back-logo .wordmark__dot { background: var(--brand-blue); }
  .contacts { position: absolute; left: 33px; top: 88px; font-family: "Open Sans", Arial, sans-serif; font-size: 11px; line-height: 14px; color: var(--muted); }
  .contacts strong { font-weight: 700; }
  .contacts li { list-style: none; margin-bottom: 10px; }
</style>
</head>
<body>
<main class="spread">
  <section class="page page--front">
    <div class="cover-panel"></div>
    <h1 class="cover-title">Brand<br>Archetype<br>Tool</h1>
    <svg class="cover-emblem" role="img" aria-label="Decorative brand emblem area" viewBox="0 0 175 295">
      <defs>
        <linearGradient id="emblemTone" x1="0" y1="1" x2="1" y2="0">
          <stop offset="0" stop-color="#3b2f6b" stop-opacity="0.55"/>
          <stop offset="1" stop-color="#3f86d6" stop-opacity="0.35"/>
        </linearGradient>
      </defs>
      <rect width="175" height="295" fill="url(#emblemTone)"/>
    </svg>
    <div class="cover-band"></div>
    <svg class="cover-photo" role="img" aria-label="Photograph of office towers seen from below" viewBox="0 0 289 186" preserveAspectRatio="none">
      <defs>
        <linearGradient id="photoTone" x1="0" y1="0" x2="1" y2="0">
          <stop offset="0" stop-color="#262626"/>
          <stop offset="0.5" stop-color="#4a4a4a"/>
          <stop offset="1" stop-color="#6e6e6e"/>
        </linearGradient>
      </defs>
      <rect width="289" height="186" fill="url(#photoTone)"/>
    </svg>
    <div class="wordmark cover-logo"><span>Brindle Harbor Partners</span><span class="wordmark__dot"></span></div>
  </section>

  <section class="page page--back">
    <article class="info-block info-block--intro">
      <h2>WHAT ARE BRAND ARCHETYPES</h2>
      <p>They express a brand as a type of person. In their way we attribute certain personalities and values to a brand based on the archetype.</p>
    </article>
    <article class="info-block info-box info-box--when">
      <h2>WHEN DO WE DO IT</h2>
      <p>We conduct archetype workshops if it becomes apparent that there is a requirement for integrating the brand promise and the brand behavior. It connects what we say with what we do as a brand. It takes place in the growth planning stage of our approach.</p>
    </article>
    <article class="info-block info-box info-box--who">
      <h2>WHO DOES IT</h2>
      <p>Key personnel from Brindle Harbor Partners do it together with key client brand stakeholders</p>
    </article>
    <footer class="back-band">
      <div class="wordmark back-logo"><span>Brindle Harbor Partners</span><span class="wordmark__dot"></span></div>
      <ul class="contacts">
        <li><strong>Singapore Office</strong><br>18 Wexley Lane, #04-12, Singapore, 000000 | ellis@brindleharbor.example</li>
        <li><strong>Melbourne Office</strong><br>Level 5, 210 Harbour Row | +61 3 9000 0000 | morgan@brindleharbor.example</li>
      </ul>
    </footer>
  </section>
</main>
</body>
</html>
```